Marnie Vale Photography needs a unique, creative business card/logo design

I need a design for business cards/logo that is unique and creative in the industry. Simplicity is nice, so not too crowded. Something that will catch my customer's eye and remain in their memory. I am primarily a landscape photographer but will be soon may be branching into boudoir photography as well. I have attached my current card.

Marnie Vale Photography
Phone: 0439 517 264
Email: MarnieValePhotography@quillmail.example
Website: www.snapnook.example/MarnieValePhotography.Aust

Marnie Vale Photography

• Contact Details on one side
• pixelation

```html
<!DOCTYPE html>
<html lang="en">
<head>
<meta charset="utf-8">
<title>Marnie Vale Photography – Business Card</title>
<link rel="stylesheet" href="https://fonts.googleapis.com/css2?family=Lato:wght@300;400;700&display=swap">
<style>
  :root {
    --backdrop: #e4e4e2;
    --card: #fbfbfa;
    --ink: #3a3a3a;
    --ink-soft: #555555;
    --icon-bg: #4a4a4a;
    --icon-glyph: #ffffff;
    --rule: #3f3f3f;
    --photo-wood: #6e5650;
    --photo-haze: #a4756a;
    --photo-foliage: #3f4a36;
    --light: #ffffff;
  }
  * { box-sizing: border-box; margin: 0; padding: 0; }
  html, body {
    width: 1200px;
    height: 800px;
    overflow: hidden;
    background: var(--backdrop);
    font-family: "Lato", "Helvetica Neue", Arial, sans-serif;
  }
  .canvas {
    width: 1200px;
    height: 800px;
    display: flex;
    align-items: center;
    justify-content: center;
  }
  .business-card {
    width: 420px;
    height: 660px;
    background: var(--card);
    border-radius: 22px;
    padding: 30px 30px 0;
    box-shadow: 0 2px 6px rgba(0,0,0,0.08);
    display: flex;
    flex-direction: column;
  }
  .hero-photo {
    position: relative;
    height: 372px;
    background:
      linear-gradient(200deg, var(--photo-foliage) 0%, rgba(63,74,54,0) 38%),
      linear-gradient(160deg, var(--photo-haze) 0%, var(--photo-wood) 55%, #4d3c38 100%);
  }
  .brand {
    position: absolute;
    left: 0;
    right: 0;
    bottom: 26px;
    display: flex;
    align-items: center;
    justify-content: center;
    gap: 14px;
    color: var(--light);
  }
  .brand-dot {
    width: 14px;
    height: 14px;
    border-radius: 50%;
    background: var(--light);
  }
  .brand-text { text-align: left; }
  .brand-name {
    font-weight: 300;
    font-size: 44px;
    line-height: 1;
    letter-spacing: 0.5px;
  }
  .brand-tagline {
    font-weight: 300;
    font-size: 13px;
    letter-spacing: 7px;
    margin-top: 6px;
  }
  .contact {
    flex: 1;
    display: flex;
    flex-direction: column;
    align-items: center;
    color: var(--ink);
    padding-top: 24px;
  }
  .contact-row {
    display: flex;
    justify-content: space-around;
    width: 100%;
  }
  .contact-item {
    display: flex;
    flex-direction: column;
    align-items: center;
    gap: 8px;
    font-size: 15px;
  }
  .contact-icon {
    width: 20px;
    height: 20px;
    border-radius: 4px;
    background: var(--icon-bg);
    display: flex;
    align-items: center;
    justify-content: center;
  }
  .contact-email { margin-top: 20px; }
  .contact-email .contact-value { font-size: 12.5px; }
  .address {
    margin-top: 20px;
    width: 100%;
    border-top: 2px solid var(--rule);
    border-bottom: 2px solid var(--rule);
    padding: 8px 0;
    text-align: center;
    font-size: 13px;
    font-weight: 400;
    line-height: 1.35;
    color: var(--ink-soft);
    letter-spacing: 0.3px;
  }
</style>
</head>
<body>
<main class="canvas">
  <article class="business-card">
    <div class="hero-photo" role="img" aria-label="Photograph of old railway sleepers receding into a misty autumn landscape">
      <div class="brand">
        <span class="brand-dot"></span>
        <div class="brand-text">
          <div class="brand-name">Marnie Vale</div>
          <div class="brand-tagline">PHOTOGRAPHY</div>
        </div>
      </div>
    </div>

    <section class="contact">
      <div class="contact-row">
        <div class="contact-item">
          <span class="contact-icon">
            <svg width="14" height="14" viewBox="0 0 14 14" aria-hidden="true">
              <rect x="2" y="5" width="10" height="7" rx="1" fill="none" stroke="var(--icon-glyph)" stroke-width="1.4"/>
              <rect x="4" y="2" width="6" height="3" fill="none" stroke="var(--icon-glyph)" stroke-width="1.2"/>
              <line x1="4" y1="8.5" x2="10" y2="8.5" stroke="var(--icon-glyph)" stroke-width="1.2"/>
            </svg>
          </span>
          <span class="contact-value">0439 517 264</span>
        </div>
        <div class="contact-item">
          <span class="contact-icon">
            <svg width="14" height="14" viewBox="0 0 14 14" aria-hidden="true">
              <rect x="4" y="1.5" width="6" height="11" rx="1.2" fill="none" stroke="var(--icon-glyph)" stroke-width="1.4"/>
              <circle cx="7" cy="10.3" r="0.8" fill="var(--icon-glyph)"/>
            </svg>
          </span>
          <span class="contact-value">0439 517 264</span>
        </div>
      </div>

      <div class="contact-item contact-email">
        <span class="contact-icon">
          <svg width="14" height="14" viewBox="0 0 14 14" aria-hidden="true">
            <text x="7" y="11" text-anchor="middle" font-family="Lato, sans-serif" font-size="11" font-weight="700" fill="var(--icon-glyph)">@</text>
          </svg>
        </span>
        <span class="contact-value">MarnieValePhotography@quillmail.example</span>
      </div>

      <address class="address">
        18TH AVENUE, 4TH FLOOR, HARBOUR CITY<br>
        HC 204, NORTHLAND
      </address>
    </section>
  </article>
</main>
</body>
</html>
```